Hypnotherapy- past life regression-life between lives therapist needs a website

I need a website that is enticing and spiritual in its feeling. It needs to have a lot of beautiful nature pictures included. The theme is "Willowmere Hollow- what could you uncover....Tides Lanterns Compass"
Because all of us have the answers to living our best life, they are in our subconcious. But not everyone is capable of accessing them. Hypnosis accesses the subconcious and helps to create new neural pathways in the brain which can create new behaviors and responses to situations.
Hypnosis can help with anxiety, pain relief, weight loss, smoking/vaping cessation, self confidence......anything about yourself that you want to change.
Exploration of past lives and life between lives can reveal things related to ones current life. For example, perhaps your fear of deep water is a result of drowning in a past life. Once this has been discovered, it can lead to changes in ones current life.
Almost any personal behavior one wants to change, can be helped through hypnotherapy.
I need a page for testimonials, a place for scheduling (I will have a link to my scheduling app) some information about hypnotherapy.
I am uploading my logo files. My business card will be using the black and gold style, but my website does not have to reflect that. It can be based on the caramel and deep green like full color logo. Earthy, calm colors.
I also like the mock up of my logo on the beach and there was one on a starry night sky that I also liked.
Target Market(s)
men and women ages 25-50
Industry/Entity Type
natural health and wellness, spirituality
Number of Pages Required
4 page
Requirements
Must have
- a page for testimonials, perhaps with a beautiful nature picture with each one, I will have approximately 6. A link to schedule a complimentary intro session, preferably on the first page
Should not have
- no swinging watches or other sterotyped hypnosis symbols

```html
<!DOCTYPE html>
<html lang="en">
<head>
<meta charset="utf-8">
<title>Willowmere Hollow – Hypnotherapy</title>
<link rel="stylesheet" href="https://fonts.googleapis.com/css2?family=Cinzel:wght@400;600;700&family=Arimo:ital,wght@0,400;0,700;1,400&display=swap">
<style>
:root{
  --board:#d5d5d5;
  --olive:#5c5f36;
  --olive-deep:#4f5430;
  --orange:#e0852a;
  --ink:#5a5b2f;
  --cream:#e8e6e0;
  --white:#ffffff;
  --note:#3b3b2c;
}
*{box-sizing:border-box;margin:0;padding:0}
html,body{width:1200px;height:3119px;overflow:hidden}
body{background:var(--board);position:relative;font-family:"Arimo",Arial,sans-serif;color:var(--ink)}
.site{position:absolute;left:74px;top:148px;width:670px;background:var(--white)}
section,header,footer{position:relative;width:670px;overflow:hidden}
.abs{position:absolute}
.display{font-family:"Cinzel",Georgia,serif}
.rule{position:absolute;height:1px;background:var(--orange)}
.btn{position:absolute;display:flex;align-items:center;justify-content:center;border-radius:16px;font-family:"Cinzel",Georgia,serif;font-weight:700;font-size:9px;color:var(--white);letter-spacing:.2px}
.btn--olive{background:var(--olive)}
.btn--orange{background:var(--orange)}
.btn--ghost{border:1.5px solid var(--white);background:transparent}

/* header */
.site-header{height:83px}
.site-header .phone{left:70px;top:20px;font-family:"Cinzel",serif;font-size:11px;color:var(--ink);display:flex;align-items:center;gap:6px;font-weight:600}
.site-header .phone b{color:var(--orange);font-weight:600}
.brand{left:274px;top:12px;width:120px;text-align:center}
.brand .mark{width:26px;height:26px;border-radius:50%;border:2px solid var(--orange);margin:0 auto 4px}
.brand .name{font-family:"Cinzel",serif;font-size:11px;font-weight:700;color:var(--orange);line-height:1.1}
.nav{top:58px;font-family:"Cinzel",serif;font-size:9px;color:var(--ink)}
.nav.active{color:var(--orange)}

/* hero */
.hero{height:330px;background:linear-gradient(180deg,#4a5a22 0%,#7a8a35 40%,#b09a40 55%,#4d4a22 100%)}
.hero .photo{inset:0;background:radial-gradient(ellipse 120px 90px at 50% 38%,rgba(250,230,140,.75),rgba(0,0,0,0) 70%)}
.hero .kicker{top:128px;width:100%;text-align:center;color:var(--white);font-size:16px;font-variant:small-caps}
.hero .title{top:148px;width:100%;text-align:center;color:var(--white);font-size:29px;font-weight:600;font-variant:small-caps}

/* offer band */
.offers{height:213px;background:var(--orange)}
.offer{width:160px;text-align:center;color:var(--white)}
.offer svg{display:block;margin:0 auto}
.offer h3{font-family:"Cinzel",serif;font-size:11px;font-weight:700;margin-top:8px}
.offer p{font-size:8px;line-height:1.5;margin-top:6px}

/* about + services */
.about{height:712px}
.about .about-title{left:70px;top:82px;font-size:23px;line-height:1.15;font-weight:700;color:var(--olive)}
.about .copy{left:70px;top:159px;width:258px;font-size:8.4px;line-height:1.45;color:var(--ink)}
.about .photo{left:358px;top:51px;width:240px;height:289px;border-radius:120px 120px 0 0;background:linear-gradient(160deg,#e8c873 0%,#a6a14a 40%,#4f6a2a 100%);box-shadow:0 6px 18px rgba(0,0,0,.18)}
.about .blob{left:565px;top:309px;width:56px;height:56px;border-radius:50%;background:var(--orange)}
.about .dots{left:362px;top:56px;width:34px;height:32px;background-image:radial-gradient(circle,var(--olive) 1.6px,transparent 1.9px);background-size:7px 7px}
.about .services-title{left:0;top:430px;width:100%;text-align:center;font-size:22px;line-height:1.2;font-weight:700;color:var(--olive)}
.service{width:110px;text-align:center;top:496px}
.service .ring{width:90px;height:90px;border:1.5px solid var(--olive);border-radius:50%;margin:0 auto;display:flex;align-items:center;justify-content:center}
.service span{display:block;margin-top:14px;font-family:"Cinzel",serif;font-size:8.5px;color:var(--ink);line-height:1.15}

/* testimonials */
.testimonials{height:266px;background:var(--olive)}
.testimonials .forest{inset:0;background:linear-gradient(180deg,rgba(255,255,255,.04),rgba(0,0,0,.08))}
.testimonials .section-title{top:38px;width:100%;text-align:center;color:var(--white);font-size:22px;font-weight:600}
.avatar{border-radius:50%;border:2px solid rgba(255,255,255,.7)}
.quote{left:327px;top:118px;width:260px;color:var(--white);font-style:italic;font-size:11px;line-height:1.3}

/* how it works */
.how{height:382px;background:var(--cream)}
.how .section-title{top:38px;width:100%;text-align:center;font-size:22px;font-weight:700;color:var(--olive)}
.step h3{font-family:"Cinzel",serif;font-size:12px;font-weight:700;color:var(--olive)}
.step p{font-size:8px;line-height:1.3;color:var(--ink);margin-top:3px}
.icon-dot{width:48px;height:48px;border-radius:50%;background:var(--olive);display:flex;align-items:center;justify-content:center}

/* videos */
.videos{height:329px}
.videos .section-title{top:30px;width:100%;text-align:center;font-size:22px;font-weight:700;color:var(--olive)}
.thumb{top:93px;width:255px;height:153px;border-radius:4px;display:flex;align-items:center;justify-content:center}
.thumb .play{width:38px;height:38px;border-radius:50%;border:2px solid var(--white);display:flex;align-items:center;justify-content:center}
.caption{top:261px;width:255px;text-align:center;font-family:"Cinzel",serif;font-size:10px;font-weight:700;color:var(--olive);line-height:1.3}

/* call to action */
.cta{height:277px;background:linear-gradient(160deg,#3c4550 0%,#b7b6b0 22%,#c27a35 45%,#d2863a 70%,#b0612a 100%)}
.cta .section-title{left:72px;top:126px;color:var(--white);font-size:23px;line-height:1.15;font-weight:600}

/* footer */
.site-footer{height:216px;background:var(--olive);color:var(--white)}
.site-footer h4{font-family:"Cinzel",serif;font-size:12px;font-weight:600}
.contact-row{left:70px;display:flex;gap:10px;align-items:flex-start;font-size:8.5px;line-height:1.3}
.contact-row i{width:20px;height:20px;border-radius:50%;background:var(--orange);display:flex;align-items:center;justify-content:center;flex:none}
.footer-brand{left:260px;top:50px;width:150px;text-align:center}
.footer-brand .mark{width:36px;height:36px;border-radius:50%;border:2px solid var(--orange);margin:0 auto 8px}
.footer-brand .name{font-family:"Cinzel",serif;font-size:15px;font-weight:700;color:var(--orange)}
.footer-about{right:72px;top:64px;width:170px;text-align:right;font-size:8.5px;line-height:1.45}
.divider{left:67px;top:174px;width:535px;height:1px;background:rgba(255,255,255,.35)}
.social{top:184px;width:12px;height:12px;border-radius:50%;border:1.5px solid var(--white)}
.copyright{top:200px;width:100%;text-align:center;font-size:8px}

/* board notes */
.note{position:absolute;left:810px;font-family:"Cinzel",serif;font-weight:600;font-size:16.5px;line-height:1.15;color:var(--note)}
.leader{position:absolute;height:1px;background:#9a9a9a}
</style>
</head>
<body>
<div class="site">

  <header class="site-header">
    <div class="abs phone">
      <svg width="13" height="13" viewBox="0 0 24 24"><circle cx="12" cy="12" r="12" fill="#5c5f36"/><path d="M8.5 6.5l2 2-1 1.5c.8 1.6 2 2.8 3.5 3.5l1.5-1 2 2-1.5 2c-3.8-.4-7.6-4.2-8-8z" fill="#fff"/></svg>
      PHONE/ TEXT: <b>555-014-2290</b>
    </div>
    <div class="abs brand"><div class="mark"></div><div class="name">WILLOWMERE<br>HOLLOW</div></div>
    <div class="btn btn--olive" style="left:489px;top:16px;width:109px;height:26px;">SCHEDULE NOW</div>
    <span class="abs nav active" style="left:70px">HOME</span>
    <span class="abs nav" style="left:121px">ABOUT US</span>
    <span class="abs nav" style="left:186px">OUR SERVICES ▾</span>
    <span class="abs nav" style="left:406px">TESTIMONIALS</span>
    <span class="abs nav" style="left:497px">VIDEOS</span>
    <span class="abs nav" style="left:553px">CONTACT</span>
  </header>

  <section class="hero">
    <div class="abs photo" role="img" aria-label="Sunlit forest path with a wooden boardwalk under mossy trees"></div>
    <p class="abs display kicker">Willowmere Hollow- what could you uncover....</p>
    <h1 class="abs display title">Tides Lanterns Compass</h1>
  </section>

  <section class="offers">
    <div class="abs offer" style="left:63px;top:30px">
      <svg width="58" height="52" viewBox="0 0 58 52" fill="none" stroke="#5c5f36" stroke-width="2"><circle cx="29" cy="20" r="14"/><path d="M8 14v18l14 14M50 14v18L36 46"/></svg>
      <h3>GUIDED HYPNOSIS</h3>
      <p>Lorem ipsum dolor sit amet, conetur adipiscing elit, sed do eiusmod tempor incididunt ut labore e, sed do eiusmod tempor incididunt loaliua.</p>
    </div>
    <div class="abs offer" style="left:254px;top:30px">
      <svg width="58" height="52" viewBox="0 0 58 52" fill="none" stroke="#5c5f36" stroke-width="2"><path d="M20 48V38c-6-3-9-9-8-16 1-9 9-15 18-14 8 1 13 7 13 14l4 8h-5v8h-8v10"/><circle cx="29" cy="22" r="7"/><circle cx="29" cy="22" r="2"/></svg>
      <h3>HYPNOTHERAPY</h3>
      <p>Lorem ipsum dolor sit amet, conetur adipiscing elit, sed do eiusmod tempor incididunt ut labore e, sed do eiusmod tempor incididunt loaliua.</p>
    </div>
    <div class="abs offer" style="left:447px;top:30px">
      <svg width="58" height="52" viewBox="0 0 58 52" fill="none" stroke="#5c5f36" stroke-width="2"><path d="M29 4c8 12 16 20 16 30a16 16 0 0 1-32 0c0-10 8-18 16-30z"/><circle cx="29" cy="34" r="8"/><circle cx="29" cy="34" r="3"/></svg>
      <h3>SELF-HYPNOSIS</h3>
      <p>Lorem ipsum dolor sit amet, conetur adipiscing elit, sed do eiusmod tempor incididunt ut labore e, sed do eiusmod tempor incididunt loaliua.</p>
    </div>
  </section>

  <section class="about">
    <h2 class="abs display about-title">ABOUT<br>HYPNOTHERAPY</h2>
    <div class="rule" style="left:8px;top:142px;width:127px"></div>
    <p class="abs copy">Lorem ipsum dolor sit amet, consectetur adipiscing elit, sed do eiusmod tempor incididunt ut labore et dolore magna aliqua. Quis ipsum suspendisse ultrices gravida. Risus commodo viverra maecenas accumsan lacus vel facilisis. Lorem ipsum dolor sit amet, consectetur adipiscing elit, sed do eiusmod tempor incididunt ut labore et dolore magna aliqua. Ut enim ad minim veniam, quis nostrud exercitation ullamco laboris nisi ut aliquip ex ea commodo consequat. Duis aute irure dolor in reprehenderit in voluptate velit esse cillum dolore eu fugiat nulla pariatur. Excepteur sint occaecat cupidatat non proident, sunt in culpa qui officia deserunt mollit anim id est laborum.</p>
    <div class="btn btn--orange" style="left:70px;top:302px;width:85px;height:28px;">READ MORE</div>
    <div class="abs blob"></div>
    <div class="abs photo" role="img" aria-label="Woman sitting in a sunlit meadow, eyes closed, at golden hour"></div>
    <div class="abs dots"></div>

    <h2 class="abs display services-title">OUR SERVICES CAN HELP WITH:</h2>
    <div class="rule" style="left:271px;top:464px;width:125px"></div>
    <svg class="abs" style="left:70px;top:533px" width="10" height="16" viewBox="0 0 10 16"><path d="M8 2L2 8l6 6" fill="none" stroke="#4f5430" stroke-width="2"/></svg>
    <svg class="abs" style="left:600px;top:533px" width="10" height="16" viewBox="0 0 10 16"><path d="M2 2l6 6-6 6" fill="none" stroke="#4f5430" stroke-width="2"/></svg>
    <div class="abs service" style="left:84px"><div class="ring"><svg width="44" height="44" viewBox="0 0 44 44" fill="none" stroke="#5c5f36" stroke-width="1.6"><path d="M14 40V31c-5-3-7-8-6-14 1-7 8-12 15-11 7 1 12 6 12 13l3 7h-4v6h-7v8"/><path d="M22 12l-3 6h5l-3 6"/></svg></div><span>ANXIETY<br>REDUCTION</span></div>
    <div class="abs service" style="left:218px"><div class="ring"><svg width="44" height="44" viewBox="0 0 44 44" fill="none" stroke="#5c5f36" stroke-width="1.6"><path d="M14 40V31c-5-3-7-8-6-14 1-7 8-12 15-11 7 1 12 6 12 13l3 7h-4v6h-7v8"/><circle cx="22" cy="18" r="7"/><circle cx="22" cy="18" r="3.5"/><circle cx="22" cy="18" r="1"/></svg></div><span>PAIN RELIEF</span></div>
    <div class="abs service" style="left:351px"><div class="ring"><svg width="44" height="44" viewBox="0 0 44 44" fill="none" stroke="#5c5f36" stroke-width="1.6"><path d="M12 4c2 8 2 14-1 20 0 8 4 14 11 16 7-2 11-8 11-16-3-6-3-12-1-20"/><path d="M4 16h8M36 16h-8"/><circle cx="22" cy="20" r="1"/></svg></div><span>WEIGHT LOSS</span></div>
    <div class="abs service" style="left:484px"><div class="ring"><svg width="44" height="44" viewBox="0 0 44 44" fill="none" stroke="#5c5f36" stroke-width="1.6"><circle cx="22" cy="20" r="4"/><path d="M22 4v10M18 8l4-4 4 4M8 30l8-6 6 4 6-4 8 6M10 38h24"/></svg></div><span>SELF CONFIDENCE<br>IMPROVEMENT</span></div>
    <div class="btn btn--orange" style="left:276px;top:646px;width:116px;height:29px;">VIEW ALL SERVICES</div>
  </section>

  <section class="testimonials">
    <div class="abs forest" role="img" aria-label="Faint misty pine forest backdrop"></div>
    <h2 class="abs display section-title">TESTIMONIALS</h2>
    <div class="rule" style="left:272px;top:74px;width:125px"></div>
    <div class="abs avatar" style="left:118px;top:127px;width:60px;height:60px;background:#8a8c6a" role="img" aria-label="Portrait of a client"></div>
    <div class="abs avatar" style="left:217px;top:127px;width:60px;height:60px;background:#9a9a86" role="img" aria-label="Portrait of a client"></div>
    <div class="abs avatar" style="left:167px;top:121px;width:72px;height:72px;background:#6e7a5a;border-color:#fff" role="img" aria-label="Portrait of a smiling client"></div>
    <p class="abs quote">“ Lorem ipsum dolor sit amet, consectetur adipis elit, sed do eiusmod tempor incididunt ut labore et dolore magna aliqua. Quis ipsum suspendisse ultric es gravida isus commodo viverra maecenas accum san lacus vel facilisis. ”</p>
  </section>

  <section class="how">
    <h2 class="abs display section-title">HOW IT WORKS</h2>
    <div class="rule" style="left:272px;top:75px;width:125px"></div>
    <svg class="abs" style="left:230px;top:60px" width="210" height="200" viewBox="0 0 210 200"><circle cx="104" cy="101" r="68" fill="none" stroke="#e0852a" stroke-width="5"/></svg>
    <div class="abs" style="left:290px;top:118px;width:88px;height:88px;border-radius:50%;background:#d8cdb9" role="img" aria-label="Spiral seashell emblem"></div>
    <div class="abs icon-dot" style="left:213px;top:116px"><svg width="24" height="24" viewBox="0 0 24 24"><path d="M6 3l4 4-2 3c1.5 3 3 4.5 6 6l3-2 4 4-3 3C10 20 4 14 3 6z" fill="#fff"/></svg></div>
    <div class="abs icon-dot" style="left:403px;top:116px"><svg width="24" height="24" viewBox="0 0 24 24"><path d="M12 2c3 3 4 7 3 12H9C8 9 9 5 12 2z" fill="#fff"/><circle cx="12" cy="9" r="1.6" fill="#5c5f36"/><path d="M9 14l-3 4h4M15 14l3 4h-4M11 16h2v5h-2z" fill="#fff"/></svg></div>
    <div class="abs icon-dot" style="left:310px;top:221px"><svg width="26" height="26" viewBox="0 0 26 26" fill="#fff"><path d="M6 4l3 4H7v6H5V8H3zM13 2l3 4h-2v8h-2V6h-2zM20 4l3 4h-2v6h-2V8h-2z"/><circle cx="6" cy="18" r="2"/><circle cx="13" cy="18" r="2"/><circle cx="20" cy="18" r="2"/><path d="M3 24a3 3 0 0 1 6 0zM10 24a3 3 0 0 1 6 0zM17 24a3 3 0 0 1 6 0z"/></svg></div>
    <div class="abs step" style="left:50px;top:112px;width:150px;text-align:right"><h3>BOOK A FREE CALL</h3><p>Lorem ipsum dolor sit amet, cons ectetur adipiscing elit, sed do eiusmod tempor incididunt ut labore et dolore magna aliqua. Quis ipsum suspendisse ultrices gravidisus commodo viverra</p></div>
    <div class="abs step" style="left:465px;top:112px;width:150px"><h3>LET CHANGE BEGIN</h3><p>Lorem ipsum dolor sit amet, cons ectetur adipiscing elit, sed do eiusmod tempor incididunt ut labore et dolore magna aliqua. Quis ipsum suspendisse ultrices gravidisus commodo viverra</p></div>
    <div class="abs step" style="left:235px;top:284px;width:200px;text-align:center"><h3>PLAN YOUR SUCCESS</h3><p>Lorem ipsum dolor sit amet, cons ectetur adipiscing elit, sed do eiusmod tempor incididunt ut labore et dolore magna aliqua. Quis ipsum suspendisse ultrices gravidisus</p></div>
  </section>

  <section class="videos">
    <h2 class="abs display section-title">VIDEOS</h2>
    <div class="rule" style="left:291px;top:64px;width:88px"></div>
    <div class="abs thumb" style="left:70px;background:linear-gradient(180deg,#dfe6e4 0%,#b9c08a 45%,#6e8f2e 100%)" role="img" aria-label="Woman with open arms in a green meadow at sunrise"><div class="play"><svg width="14" height="14" viewBox="0 0 14 14"><path d="M3 1l10 6-10 6z" fill="#fff"/></svg></div></div>
    <div class="abs thumb" style="left:342px;background:linear-gradient(160deg,#2c3a22 0%,#5b5a36 50%,#c9a27a 100%)" role="img" aria-label="Woman relaxing with eyes closed among tropical leaves"><div class="play"><svg width="14" height="14" viewBox="0 0 14 14"><path d="M3 1l10 6-10 6z" fill="#fff"/></svg></div></div>
    <p class="abs caption" style="left:70px">LOREM IPSUM DOLOR SIT AMET,<br>CONSECTETUR ADIPISCING</p>
    <p class="abs caption" style="left:342px">LOREM IPSUM DOLOR SIT AMET,<br>CONSECTETUR ADIPISCING</p>
    <div class="abs" style="left:580px;top:170px;width:55px;height:120px;border-radius:28px;background:linear-gradient(180deg,rgba(224,133,42,.15),rgba(224,133,42,.35))" role="img" aria-label="Trail of small footprints"></div>
  </section>

  <section class="cta" role="img" aria-label="Footprints along a sandy beach at the water's edge">
    <h2 class="abs display section-title">SCHEDULE YOUR FREE<br>CONSULTATION NOW.</h2>
    <div class="btn btn--ghost" style="left:72px;top:191px;width:109px;height:26px;font-weight:600">SCHEDULE NOW</div>
  </section>

  <footer class="site-footer">
    <h4 class="abs" style="left:72px;top:32px">CONTACT US</h4>
    <div class="abs contact-row" style="top:62px"><i><svg width="10" height="12" viewBox="0 0 10 12"><path d="M5 0a4 4 0 0 1 4 4c0 3-4 8-4 8S1 7 1 4a4 4 0 0 1 4-4z" fill="#fff"/><circle cx="5" cy="4" r="1.5" fill="#e0852a"/></svg></i><span>P.O. Box 418 Fernwood Lane<br>Cedar Glen Studio</span></div>
    <div class="abs contact-row" style="top:94px"><i><svg width="11" height="11" viewBox="0 0 24 24"><path d="M6 3l4 4-2 3c1.5 3 3 4.5 6 6l3-2 4 4-3 3C10 20 4 14 3 6z" fill="#fff"/></svg></i><span>Phone/ Text<br>555-014-2290</span></div>
    <div class="abs contact-row" style="top:126px"><i><svg width="11" height="9" viewBox="0 0 11 9"><rect x=".5" y=".5" width="10" height="8" fill="#fff"/><path d="M.5 .5l5 4 5-4" fill="none" stroke="#e0852a"/></svg></i><span>Email:<br>hello@willowmerehollow.com</span></div>
    <div class="abs footer-brand"><div class="mark"></div><div class="name">WILLOWMERE<br>HOLLOW</div></div>
    <h4 class="abs" style="right:72px;top:32px">ABOUT US</h4>
    <p class="abs footer-about">Lorem ipsum dolor sit amet, con sectetur adipiscing elit, sed do eius mod tempor incididunt ut labore et dolore magna aliqua. Quis ipsum sus pendisse ultrices gravida. Risus commodo viverra maecen</p>
    <div class="abs divider"></div>
    <div class="abs social" style="left:322px"></div>
    <div class="abs social" style="left:338px"></div>
    <p class="abs copyright">Copyright © 2024 WillowmereHollow.com - All rights reserved</p>
  </footer>
</div>

<div class="leader" style="left:694px;top:1313px;width:111px"></div>
<p class="note" style="top:1293px">YES, THE ARROWS DISPLAY<br>THE ALL SERVICES.</p>
<div class="leader" style="left:466px;top:1434px;width:339px"></div>
<p class="note" style="top:1414px">YES, WHEN CLICK THE BUTTON<br>ITS GOING TO ANOTHER PAGE</p>
</body>
</html>
```